Web design for a food truck business

We need a web design for an established food truck business who have an active Pagebook following but no website. We are a digital marketing agency and the client is looking for a website that stands out and doesn't have a corporate or boring look to it.
The client's facebook page is: https://www.facebook.com/DonTortaVelaroy/

Number of Pages Required

1 page

```html
<!DOCTYPE html>
<html lang="en">
<head>
<meta charset="utf-8">
<title>Don Torta – Food Truck</title>
<link href="https://fonts.googleapis.com/css2?family=Lato:ital,wght@0,400;0,700;0,900;1,400&display=swap" rel="stylesheet">
<style>
:root{
  --yellow:#f4e36d;
  --cream:#faf3cf;
  --red:#b3152c;
  --red-dark:#9e1024;
  --gold:#e7c85a;
  --ink:#222;
  --grey-card:#efefef;
  --white:#fff;
}
*{box-sizing:border-box;margin:0;padding:0}
html,body{width:1200px;height:3327px;overflow:hidden}
body{font-family:"Lato",sans-serif;color:var(--ink);position:relative;background:var(--white)}
.abs{position:absolute}
.section-title{position:absolute;left:0;width:1200px;text-align:center;font-weight:900;font-size:36px;color:var(--red);letter-spacing:.5px}

/* header */
.header{left:0;top:0;width:1200px;height:477px;background:var(--yellow)}
.brand{left:133px;top:52px;width:410px;height:160px;display:flex;align-items:center;justify-content:center;gap:14px}
.brand-dot{width:26px;height:26px;border-radius:50%;background:var(--red)}
.brand-name{font-weight:900;font-size:52px;color:var(--red);letter-spacing:1px}
.nav{left:643px;top:90px;display:flex;gap:30px;font-size:17px;color:var(--ink)}
.welcome{left:40px;top:232px;width:594px;text-align:center}
.welcome h1{font-size:31px;font-weight:700;margin-bottom:14px}
.welcome p{font-size:22px;line-height:28px}
.btn-book{left:197px;top:370px;width:280px;height:47px;border-radius:24px;background:var(--red);color:var(--white);font-size:15px;font-weight:700;display:flex;align-items:center;justify-content:center;letter-spacing:.3px}
.hero-photo{left:614px;top:151px;width:524px;height:330px;background:linear-gradient(135deg,#e9eef2,#7b8794 55%,#3a3f45);border:3px solid #fff}
.band-pattern{left:0;width:1200px;background:linear-gradient(180deg,var(--yellow) 0,var(--yellow) 15%,var(--red) 15%,var(--red) 30%,#f0b52a 30%,#f0b52a 38%,#3aa1cc 38%,#3aa1cc 44%,var(--red) 44%,var(--red) 100%)}

/* menu */
.menu{left:0;top:677px;width:1200px;height:470px;background:var(--cream)}
.card{position:absolute;top:113px;width:331px;text-align:center}
.card-img{width:331px;height:177px}
.card h3{margin-top:22px;font-size:20px;font-weight:900;color:var(--red)}
.card p{margin-top:8px;font-size:15px;line-height:25px;padding:0 18px}
.arrow{position:absolute;top:280px;width:16px;height:20px}

/* events */
.events{left:0;top:1147px;width:1200px;height:503px;background:var(--white)}
.events .lead{position:absolute;top:102px;width:1200px;text-align:center;font-size:15px}
.tile{position:absolute;top:153px;width:331px;height:268px;display:flex;align-items:center;justify-content:center;color:var(--white);font-weight:900;font-size:24px}

/* speciality */
.speciality{left:0;top:1650px;width:1200px;height:435px;background:radial-gradient(ellipse at 25% 45%,#fffbe6 0,#fcf2c9 70%)}
.churro-img{left:89px;top:47px;width:499px;height:333px;border-radius:40% 60% 50% 50%/45% 40% 60% 55%;background:linear-gradient(160deg,#e7a15e,#c77232 60%,#a9572a)}
.speciality h2{left:614px;top:86px;font-size:34px;font-weight:900;color:var(--red)}
.speciality p{left:614px;top:140px;width:520px;font-size:15px;line-height:31px}
.btn-more{left:614px;top:291px;width:180px;height:49px;border-radius:25px;background:var(--gold);font-weight:700;font-size:15px;display:flex;align-items:center;justify-content:center;color:var(--ink)}

/* testimonials */
.testimonials{left:0;top:2085px;width:1200px;height:532px;background:var(--white)}
.quote{position:absolute;top:144px;width:331px;height:266px;background:var(--grey-card);border-radius:14px;padding:28px 20px}
.quote p{font-style:italic;font-size:14.5px;line-height:28px}
.quote h4{margin-top:24px;font-size:15px;font-weight:900;color:var(--red)}
.quote .mark{position:absolute;left:20px;top:192px;font-size:130px;font-family:Georgia,serif;font-weight:700;color:#d8d8d8;line-height:1;height:74px;overflow:hidden}
.avatar{position:absolute;right:28px;bottom:-40px;width:80px;height:80px;border-radius:50%;border:4px solid #fff;background:linear-gradient(160deg,#d9c3a8,#8a7560)}

/* clients */
.clients{left:0;top:2617px;width:1200px;height:267px;background:var(--cream)}
.client{position:absolute;top:167px;font-weight:700;font-size:22px;color:#555;display:flex;align-items:center;gap:8px}
.client-sq{width:18px;height:18px;background:#555}

/* footer */
.footer{left:0;top:3028px;width:1200px;height:299px;background:var(--red)}
.footer h5{position:absolute;top:32px;font-size:17px;font-weight:900;color:var(--gold);letter-spacing:.5px}
.footer ul{position:absolute;list-style:none;font-size:14px;color:var(--white);line-height:29px}
.hours{position:absolute;top:64px;left:350px;font-size:14px;color:var(--white);line-height:33px}
.hours span{display:inline-block;width:135px}
.social{position:absolute;left:723px;top:68px;display:flex;gap:12px;font-size:13px;font-weight:700;color:var(--white)}
.copy{position:absolute;left:723px;top:126px;font-size:12px;color:var(--white);line-height:20px}
.footer-wave{left:0;top:3238px;width:1200px;height:89px}
.footer-brand{left:500px;top:3238px;width:200px;height:80px;display:flex;align-items:center;justify-content:center;font-weight:900;font-size:26px;color:var(--red)}
</style>
</head>
<body>

<header class="abs header">
  <div class="abs brand"><span class="brand-dot"></span><span class="brand-name">DON TORTA</span></div>
  <nav class="abs nav"><span>Home</span><span>About Us</span><span>Catering Menu</span><span>Events</span><span>Contact Us</span></nav>
  <div class="abs welcome">
    <h1>Welcome To Don Torta</h1>
    <p>Neque porro quisquam est qui dolorem ipsum quia<br>dolor sit amet, consectetur, adipisci velit...</p>
  </div>
  <div class="abs btn-book">BOOK US FOR YOUR EVENT</div>
  <div class="abs hero-photo" role="img" aria-label="Food truck serving window with staff and customers"></div>
</header>

<div class="abs band-pattern" style="top:477px;height:200px" role="img" aria-label="Decorative zigzag and folk pattern band in red, yellow and blue"></div>

<section class="abs menu">
  <div class="section-title" style="top:44px">FESTIVAL MENU</div>
  <svg class="arrow" style="left:50px" viewBox="0 0 16 20"><path d="M12 2 4 10l8 8" fill="none" stroke="#333" stroke-width="3"/></svg>
  <svg class="arrow" style="left:1136px" viewBox="0 0 16 20"><path d="M4 2l8 8-8 8" fill="none" stroke="#333" stroke-width="3"/></svg>
  <div class="card" style="left:75px"><div class="card-img" role="img" aria-label="Churros with chocolate filling" style="background:linear-gradient(135deg,#e7b06b,#a8642d)"></div><h3>SED A LECTUS</h3><p>Lorem ipsum dolor sit amet, consectetur adipiscing elit. Mauris vitae tortor ut orci feugiat malesuada.</p></div>
  <div class="card" style="left:435px"><div class="card-img" role="img" aria-label="Filled sandwich roll held in hand" style="background:linear-gradient(135deg,#d9b07c,#8b4a2c 60%,#5c7a3b)"></div><h3>SED A LECTUS</h3><p>Lorem ipsum dolor sit amet, consectetur adipiscing elit. Mauris vitae tortor ut orci feugiat malesuada.</p></div>
  <div class="card" style="left:796px"><div class="card-img" role="img" aria-label="Chocolate coated dessert" style="background:linear-gradient(135deg,#7a4326,#3b1c10)"></div><h3>SED A LECTUS</h3><p>Lorem ipsum dolor sit amet, consectetur adipiscing elit. Mauris vitae tortor ut orci feugiat malesuada.</p></div>
</section>

<section class="abs events">
  <div class="section-title" style="top:38px">EVENTS</div>
  <div class="lead">Lorem ipsum dolor sit amet, consectetur adipiscing elit. Mauris vitae tortor ut orci feugiat malesuada.</div>
  <div class="tile" style="left:75px;background:linear-gradient(160deg,#5a3a2e,#2e1f1a)" role="img" aria-label="Birthday party table scene">BIRTHDAYS EVENTS</div>
  <div class="tile" style="left:435px;background:linear-gradient(160deg,#3c4a5e,#1d2430)" role="img" aria-label="Wedding marquee at dusk">WEDDINGS EVENTS</div>
  <div class="tile" style="left:796px;background:linear-gradient(160deg,#6b6f64,#2f3a2a)" role="img" aria-label="Outdoor lunch seating area">WORK LUNCHES</div>
</section>

<section class="abs speciality">
  <div class="abs churro-img" role="img" aria-label="Two sugared churros"></div>
  <h2 class="abs">OUR SPECIALITY</h2>
  <p class="abs">Lorem ipsum dolor sit amet, consectetur adipiscing elit. Mauris vitae tortor ut orci feugiat malesuada. Mauris nec suscipit tortor. Phasellus finibus nisi a risus sagittis, et porta dui consequat. Pellentesque ante orci, tincidunt sit amet tristique a, ornare nec felis.</p>
  <div class="abs btn-more">READ MORE</div>
</section>

<section class="abs testimonials">
  <div class="section-title" style="top:72px">TESTIMONIALS</div>
  <div class="quote" style="left:75px"><p>Lorem ipsum dolor sit amet, consectetur adipiscing elit. Mauris vitae tortor ut orci feugiat malesuada. Mauris nec suscipit tortor phasellus finibus nisi a risus sagittis, et porta dui consequat.</p><h4>-NAME HEADING</h4><div class="mark">“</div><div class="avatar" role="img" aria-label="Customer portrait"></div></div>
  <div class="quote" style="left:435px"><p>Lorem ipsum dolor sit amet, consectetur adipiscing elit. Mauris vitae tortor ut orci feugiat malesuada. Mauris nec suscipit tortor phasellus finibus nisi a risus sagittis, et porta dui consequat.</p><h4>-NAME HEADING</h4><div class="mark">“</div><div class="avatar" role="img" aria-label="Customer portrait"></div></div>
  <div class="quote" style="left:796px"><p>Lorem ipsum dolor sit amet, consectetur adipiscing elit. Mauris vitae tortor ut orci feugiat malesuada. Mauris nec suscipit tortor phasellus finibus nisi a risus sagittis, et porta dui consequat.</p><h4>-NAME HEADING</h4><div class="mark">“</div><div class="avatar" role="img" aria-label="Customer portrait"></div></div>
</section>

<section class="abs clients">
  <div class="section-title" style="top:58px">OUR CLIENTS</div>
  <div class="client" style="left:105px">Bramblebay</div>
  <div class="client" style="left:318px">Harrowmill</div>
  <div class="client" style="left:520px">kindred hearts</div>
  <div class="client" style="left:748px"><span class="client-sq"></span>Arlow Cover</div>
  <div class="client" style="left:958px">platewise</div>
</section>

<div class="abs band-pattern" style="top:2884px;height:144px" role="img" aria-label="Decorative folk pattern band in red, yellow and blue"></div>

<footer class="abs footer">
  <h5 style="left:75px">QUICK LINKS</h5>
  <ul style="left:75px;top:62px"><li>Home</li><li>About Us</li><li>Menu</li><li>Services</li><li>Events</li></ul>
  <ul style="left:209px;top:62px"><li>Gallery</li><li>Blog</li><li>Contact Us</li></ul>
  <h5 style="left:350px">HOURS</h5>
  <div class="hours"><div><span>Monday - Friday:</span>10am - 8 pm</div><div><span>Saturday:</span>12pm- 10pm</div><div><span>Sunday:</span>Closed</div></div>
  <h5 style="left:723px">FOLLOW US</h5>
  <div class="social"><span>Pagebook</span><span>Chirper</span><span>Snapgram</span><span>Linkwork</span><span>Tubecast</span></div>
  <div class="copy">Copyright © 2016 Company Name<br>All Right Reserved</div>
</footer>
<svg class="abs footer-wave" viewBox="0 0 1200 89" preserveAspectRatio="none"><path d="M0 60 C150 20 300 80 450 45 C550 20 560 0 600 0 C640 0 650 20 750 45 C900 80 1050 20 1200 60 V89 H0Z" fill="#e7c85a"/></svg>
<div class="abs footer-brand">DON TORTA</div>

</body>
</html>
```